Real Estate Website

The existing website design is http://brevanola.quillset4.com.au/ and we are not happy with it and need a fresh new design.

The menu of the website should be as it is however the content on the home page needs to include the following:

* Some sort of feature image/slideshow
* Introduction text and photo
* Our services section with boxes for 'strata management' 'property management' and 'property valuation & brokerage'. These boxes will then link to specific areas in the website
* Where are we with the contact details
* contact us with a form asking for name, email, phone, service interested in (as a dropdown) and comments box.
(do not include the who we are section)

In regards to design style/layout, here is what we like:
https://tarnelbeans.com/us/
https://www.coverlyne.com.au/
https://www.pendrake.com.au/
https://www.hqz.com/
https://www.vornelli.com.au/

```html
<!DOCTYPE html>
<html lang="en">
<head>
<meta charset="utf-8">
<title>Harlow &amp; Finch — Property Management</title>
<link rel="stylesheet" href="https://fonts.googleapis.com/css2?family=Libre+Baskerville:wght@400;700&family=Libre+Franklin:wght@400;500;600&display=swap">
<style>
:root{
  --navy:#0c1050;
  --ink:#1a1e5a;
  --text:#2b2e4a;
  --mist:#eef0f7;
  --lilac:#9ea6dd;
  --white:#ffffff;
  --line:#c9cde3;
}
*{box-sizing:border-box;margin:0;padding:0}
html,body{width:1200px;height:4944px;overflow:hidden}
body{position:relative;background:var(--white);font-family:"Libre Baskerville",Georgia,serif;color:var(--text)}
.abs{position:absolute}
.btn{position:absolute;display:flex;align-items:center;justify-content:center;font-family:"Libre Franklin",Arial,sans-serif;font-size:12px;font-weight:500;letter-spacing:.3px;text-transform:uppercase}
.btn-dark{background:var(--navy);color:var(--white)}

.site-header{position:absolute;left:0;top:0;width:1200px;height:62px;background:var(--white);z-index:3}
.brand{position:absolute;left:28px;top:13px;font-family:"Libre Baskerville",Georgia,serif;font-weight:700;font-size:28px;color:#2a3a9a}
.nav-item{position:absolute;top:25px;font-family:"Libre Franklin",Arial,sans-serif;font-size:10px;text-transform:uppercase;color:var(--navy)}
.nav-item.active{color:#4a55b0}
.client-login{position:absolute;left:1032px;top:0;width:168px;height:62px;background:var(--navy);color:var(--white);font-family:"Libre Franklin",Arial,sans-serif;font-size:10px;display:flex;align-items:center;justify-content:center;text-transform:uppercase}
.dropdown{position:absolute;left:645px;top:63px;width:158px;height:64px;background:var(--mist);z-index:4;font-family:"Libre Franklin",Arial,sans-serif;font-size:9.5px;text-transform:uppercase}
.dropdown span{position:absolute;left:22px;color:var(--navy)}

.hero{position:absolute;left:0;top:62px;width:1200px;height:456px;background:linear-gradient(160deg,#c7ccd3 0%,#8d949c 35%,#3e4650 70%,#5d6a55 100%)}
.hero h1{position:absolute;left:223px;top:162px;width:460px;font-family:"Libre Franklin",Arial,sans-serif;font-weight:400;font-size:22px;line-height:30px;color:var(--white)}
.hero .btn-light{left:223px;top:245px;width:134px;height:35px;background:var(--white);color:var(--navy)}
.hero .btn-outline{left:368px;top:245px;width:203px;height:35px;border:2px solid var(--white);color:var(--white)}
.slider-bar{position:absolute;top:434px;height:3px;background:rgba(255,255,255,.75)}
.slider-bar.current{background:#2c3480}

.scroll-band{position:absolute;left:0;top:518px;width:1200px;height:62px;background:var(--white);border-bottom:1px solid var(--line)}
.scroll-band span{position:absolute;left:0;width:1200px;top:16px;text-align:center;font-family:"Libre Franklin",Arial,sans-serif;font-size:10px;color:var(--navy)}

.welcome{position:absolute;left:0;top:580px;width:1200px;height:864px;background:var(--mist)}
.welcome-photo{position:absolute;left:0;top:102px;width:574px;height:382px;background:linear-gradient(120deg,#9aa6b4,#d8dde3 45%,#b7b0a4 75%,#6e7884)}
.welcome h2{position:absolute;left:624px;top:96px;font-family:"Libre Franklin",Arial,sans-serif;font-weight:400;font-size:28px;color:var(--ink)}
.welcome-copy{position:absolute;left:624px;top:168px;width:522px;font-size:14.5px;line-height:22.5px;color:var(--text)}
.welcome-copy p{margin-bottom:14px}

.services{position:absolute;left:0;top:1444px;width:1200px;height:1551px;background:var(--mist);border-top:1px solid var(--line)}
.services h2{position:absolute;left:0;width:1200px;top:95px;text-align:center;font-family:"Libre Franklin",Arial,sans-serif;font-weight:400;font-size:28px;color:var(--ink)}
.service-card{position:absolute;left:225px;width:750px;height:374px;background:var(--white);box-shadow:0 2px 6px rgba(20,25,80,.15)}
.service-photo{position:absolute;top:0;width:313px;height:374px}
.service-body{position:absolute;top:22px;width:392px}
.service-body h3{font-family:"Libre Franklin",Arial,sans-serif;font-weight:500;font-size:21px;color:var(--ink);margin-bottom:26px}
.service-body p{font-size:14px;line-height:22px;margin-bottom:15px;color:var(--text)}
.service-body .btn{position:relative;width:148px;height:36px;margin-top:10px}

.location{position:absolute;left:0;top:2995px;width:1200px;height:580px;background:var(--mist);border-top:1px solid var(--line)}
.map{position:absolute;left:0;top:0;width:600px;height:580px;background:linear-gradient(135deg,#e9ecef,#dde2e6 50%,#e6e9e2)}
.location h2{position:absolute;left:649px;top:60px;font-family:"Libre Franklin",Arial,sans-serif;font-weight:400;font-size:28px;color:var(--ink)}
.loc-text{position:absolute;left:649px;font-family:"Libre Franklin",Arial,sans-serif;font-size:18px;line-height:29px;color:var(--navy)}
.loc-icon{position:absolute}

.contact{position:absolute;left:0;top:3575px;width:1200px;height:776px;background:var(--lilac)}
.contact h2{position:absolute;left:0;width:1200px;top:104px;text-align:center;font-family:"Libre Franklin",Arial,sans-serif;font-weight:400;font-size:28px;color:var(--ink)}
.field{position:absolute;left:419px;width:362px;background:#eef0fa;border-radius:4px;font-family:"Libre Franklin",Arial,sans-serif;font-size:17px;color:#4b4f6e;padding:13px 12px}
.field .tag{position:absolute;left:18px;top:-7px;background:#eef0fa;padding:0 4px;font-size:8.5px;text-transform:uppercase;color:#3b3f5e;border-radius:2px}
.contact .btn{left:526px;top:639px;width:148px;height:37px}

.site-footer{position:absolute;left:0;top:4351px;width:1200px;height:593px;background:var(--navy)}
.foot-col{position:absolute;top:55px;font-family:"Libre Franklin",Arial,sans-serif;color:var(--white)}
.foot-col h4{font-weight:400;font-size:12px;text-transform:uppercase;margin-bottom:24px}
.foot-col a{display:block;font-size:12px;line-height:31.3px;color:var(--white);text-decoration:none}
.social{position:absolute;top:4609px;width:22px;height:22px;border:2px solid #8e93bd;border-radius:50%}
.foot-brand{position:absolute;left:0;width:1200px;top:4866px;text-align:center;font-family:"Libre Baskerville",Georgia,serif;font-weight:700;font-size:23px;color:var(--white)}
.foot-small{position:absolute;top:4880px;font-family:"Libre Franklin",Arial,sans-serif;font-size:8px;color:#c6c9e4}
</style>
</head>
<body>

<header class="site-header">
  <div class="brand">Harlow &amp; Finch</div>
  <span class="nav-item" style="left:408px">Strata ▾</span>
  <span class="nav-item" style="left:508px">Rentals ▾</span>
  <span class="nav-item active" style="left:617px">Insurance and Valuations ▾</span>
  <span class="nav-item" style="left:828px">About us ▾</span>
  <span class="nav-item" style="left:942px">Contact us</span>
  <div class="client-login">Client Login</div>
</header>
<nav class="dropdown">
  <span style="top:11px">Insurance Services</span>
  <span style="top:41px;color:#4a55b0">Valuation Services</span>
</nav>

<section class="hero">
  <div class="abs" role="img" aria-label="Modern apartment building with balconies and palm trees" style="inset:0"></div>
  <h1>Over 120 years of experience in Property Management at your service</h1>
  <div class="btn btn-light">Get a quote</div>
  <div class="btn btn-outline">Explore our services</div>
  <svg class="abs" style="left:30px;top:210px" width="24" height="40" viewBox="0 0 24 40"><path d="M18 4 4 20l14 16" fill="none" stroke="#fff" stroke-width="2"/></svg>
  <svg class="abs" style="left:1146px;top:210px" width="24" height="40" viewBox="0 0 24 40"><path d="M6 4l14 16L6 36" fill="none" stroke="#fff" stroke-width="2"/></svg>
  <div class="slider-bar" style="left:269px;width:130px"></div>
  <div class="slider-bar" style="left:426px;width:92px"></div>
  <div class="slider-bar current" style="left:547px;width:106px"></div>
  <div class="slider-bar" style="left:672px;width:104px"></div>
  <div class="slider-bar" style="left:799px;width:101px"></div>
</section>

<div class="scroll-band">
  <span>SCROLL</span>
  <svg class="abs" style="left:587px;top:35px" width="26" height="14" viewBox="0 0 26 14"><path d="M1 1l12 11L25 1" fill="none" stroke="#0c1050" stroke-width="1.5"/></svg>
</div>

<section class="welcome">
  <div class="welcome-photo" role="img" aria-label="Business people shaking hands across an office desk"></div>
  <h2>Welcome to Harlow &amp; Finch</h2>
  <div class="welcome-copy">
    <p>Harlow &amp; Finch was formed in 1901 by the then 24 year old J W Harlow, later to become a well-known local figure. The company grew on the strength of its management department and the successful Auction of residential subdivisions in the developing suburbs of Ashcombe, Wrenfield, Kensingvale and Dunmore.</p>
    <p>In 1926 the company was acquired by Hugh Finch, who continued the growth of the business throughout his stewardship. Intent on a family enterprise he encouraged his sons Arthur, Jonas and Gerald to join him. Arthur's son Douglas continued the family tradition, owning and managing the business until his retirement in 2004. Today the company continues under the guidance of Edward Finch, grandson of Arthur.</p>
    <p>With over a century of experience in the eastern suburbs real estate market our aim is to provide clients with expert advice on Strata, Company Title, Property Management &amp; Building Valuations (for insurance purposes) with old-fashioned honesty and integrity.</p>
    <p>The company continues with a strong management base of over 400 strata buildings and an expert staff to advise on your real estate needs. Now well into its second century of operation the tradition of personal service and integrity is being preserved and expanded into the new millennium.</p>
  </div>
  <div class="btn btn-dark" style="left:624px;top:724px;width:154px;height:36px">Meet our team</div>
</section>

<section class="services">
  <h2>Our Services</h2>

  <article class="service-card" style="top:223px">
    <div class="service-photo" role="img" aria-label="Business meeting around a conference table" style="left:0;background:linear-gradient(135deg,#8b94a8,#c9cdd8 50%,#5d667c)"></div>
    <div class="service-body" style="left:337px">
      <h3>Strata Management</h3>
      <p>Nervous about your property adventure? Don't be. Whether you're getting ready to buy or sell, in the middle of it, or just looking for some answers, our top-notch skills ensure you get the best experience possible.</p>
      <p>It's what we love to do.</p>
      <div class="btn btn-dark">Find out more</div>
    </div>
  </article>

  <article class="service-card" style="top:649px">
    <div class="service-body" style="left:24px">
      <h3>Property Management</h3>
      <p>Large or small, condo or mansion, we can find it and get it for you at the price that's right.</p>
      <p>TICs? Fixer-uppers? Luxury?</p>
      <p>We can help with all of it. We always have a current list of available properties for you to check out.</p>
      <div class="btn btn-dark">Find out more</div>
    </div>
    <div class="service-photo" role="img" aria-label="Couple unpacking moving boxes in a new home" style="left:437px;background:linear-gradient(135deg,#5e6880,#a8aebd 50%,#7a6f6a)"></div>
  </article>

  <article class="service-card" style="top:1073px">
    <div class="service-photo" role="img" aria-label="Consultant working at a laptop in a bright office" style="left:0;background:linear-gradient(135deg,#c6cad6,#8e97ad 55%,#5a6379)"></div>
    <div class="service-body" style="left:337px">
      <h3>Property Valuation &amp; Brokerage</h3>
      <p>If you have questions about affordability, credit, legal matters, or income, trust us to find you what you need fast.</p>
      <p>We make sure you feel confident and educated every step of the way.</p>
      <div class="btn btn-dark">Find out more</div>
    </div>
  </article>
</section>

<section class="location">
  <div class="map" role="img" aria-label="Street map showing the office location"></div>
  <h2>Where are we</h2>
  <div class="loc-text" style="top:150px;font-size:20px">Harlow &amp; Finch</div>
  <div class="loc-text" style="top:196px">48 Marlow Street, Kensingvale,<br>New South Wales 2099, Australia</div>
  <div class="loc-text" style="top:273px">(02) 9000 5172</div>
  <div class="loc-text" style="top:318px">reception@harlowfinch.com.au<br>accounts@harlowfinch.com.au</div>
  <div class="loc-text" style="top:391px">Timing:<br>Mon - Fri — 9:00 am - 5:00 pm<br>Sat — 10:00 am - 4:00 pm<br>Sun — Closed</div>
  <svg class="loc-icon" style="left:962px;top:212px" width="28" height="30" viewBox="0 0 28 30" fill="none" stroke="#0c1050" stroke-width="1.5"><path d="M3 8l7-3 8 3 7-3v20l-7 3-8-3-7 3z"/><circle cx="14" cy="13" r="3"/></svg>
  <svg class="loc-icon" style="left:812px;top:275px" width="26" height="26" viewBox="0 0 26 26" fill="none" stroke="#0c1050" stroke-width="1.5"><path d="M6 2l4 5-2 3c1 3 4 6 7 7l3-2 5 4-2 4C12 24 2 14 2 5z"/></svg>
  <svg class="loc-icon" style="left:915px;top:330px" width="28" height="22" viewBox="0 0 28 22" fill="none" stroke="#0c1050" stroke-width="1.5"><rect x="1" y="1" width="26" height="20" rx="1"/><path d="M1 2l13 10L27 2"/></svg>
</section>

<section class="contact">
  <h2>Contact Us</h2>
  <div class="field" style="top:182px;height:50px"><span class="tag">Name</span>Martin Selwyn|</div>
  <div class="field" style="top:252px;height:50px">|Enter your email</div>
  <div class="field" style="top:321px;height:50px">|Enter your phone number</div>
  <div class="field" style="top:396px;height:48px"><span class="tag">Service interested in</span>Select an option
    <svg class="abs" style="left:332px;top:19px" width="18" height="10" viewBox="0 0 18 10"><path d="M1 1l8 7 8-7" fill="none" stroke="#1a1e5a" stroke-width="1.5"/></svg>
  </div>
  <div class="field" style="top:465px;height:148px">|Enter your message</div>
  <div class="btn btn-dark">Send message</div>
</section>

<footer class="site-footer">
  <div class="foot-col" style="left:225px"><h4>Home</h4><a>About Harlow &amp; Finch</a><a>Our Team</a><a>Contact Us</a><a>Customer Login</a></div>
  <div class="foot-col" style="left:411px"><h4>Strata</h4><a>Strata Management Services</a><a>New Business Quote</a><a>Update Owner Details</a><a>By-Laws</a><a>Links</a><a>Forms</a><a>Emergency Tradesman List</a><a>Maintenance Request</a><a>Paying Strata</a></div>
  <div class="foot-col" style="left:599px"><h4>Rentals</h4><a>Why Choose Us</a><a>Property Management</a><a>Residential Rentals</a><a>Commercial for Lease</a><a>Tenant Application</a><a>Maintenance Request</a><a>Vacating Form</a><a>Appraisal Request</a><a>Paying Rent</a><a>Frequently Asked Questions</a><a>Summary of Fees</a></div>
  <div class="foot-col" style="left:787px"><h4>Insurance &amp; Valuations</h4><a>Insurance Services</a><a>Valuations Services</a></div>
</footer>
<div class="social" style="left:228px"></div>
<div class="social" style="left:283px"></div>
<div class="social" style="left:338px"></div>
<div class="foot-small" style="left:24px">© 2021, Harlow &amp; Finch. All rights reserved.</div>
<div class="foot-brand">Harlow &amp; Finch</div>
<div class="foot-small" style="left:988px">Privacy Policy | Terms and Conditions | Disclaimer</div>

</body>
</html>
```